Display ads - Med spa Velmira promotion

Please create an ad creative for a promotional special for a med spa:
First-time customers who book a Velmira appointment receive $50 off the Velmira treatment

Please have an aspect of diversity in the ad (the company is black and woman-owned, so more than just white people in the ad creative

The company goes for "clean and tranquil" as part of their aesthetic

Attached here are the logo and picture of the homepage, and other images on the website, typical of the aesthetic of the company identity

you can find the website here for inspiration: thedewlinestudioct.com

Please no "black and white" photography, full color only, thank you!

Target Market(s)

New Haven, Connecticut, wealthy individuals who want to look and feel younger, want great skin, and want to feel youthful

Industry/Entity Type

Medspa/beauty

Requirements
Must have
• Need 5 sizes that fit the following Medium rectangle: 300×250; Large rectangle: 300×600 ; 728x90, 300x50; 160x600
Nice to have
• Clean, refined, bright
Should not have
• black and white photos, cartoonish, or drawn items

```html
<!DOCTYPE html>
<html lang="en">
<head>
<meta charset="utf-8">
<title>Dewline Aesthetics – Velmira Offer</title>
<link rel="stylesheet" href="https://fonts.googleapis.com/css2?family=Poppins:wght@400;600;700&display=swap">
<style>
  :root {
    --sun: #fbb900;
    --sun-deep: #f7a21c;
    --sun-light: #ffd54a;
    --ink: #0c0c0c;
    --paper: #ffffff;
    --brand-ink: #1d2a44;
    --skin-a: #d9b49a;
    --skin-b: #c59174;
  }
  * { box-sizing: border-box; margin: 0; padding: 0; }
  html, body { width: 1200px; height: 1000px; overflow: hidden; }
  body { font-family: "Poppins", sans-serif; background: var(--sun); }
  .ad {
    position: relative;
    width: 1200px;
    height: 1000px;
    overflow: hidden;
  }
  .ad__backdrop {
    position: absolute;
    inset: 0;
    background:
      radial-gradient(ellipse at 50% 40%, rgba(255,226,110,0.75), rgba(255,226,110,0) 60%),
      linear-gradient(160deg, var(--sun-light) 0%, var(--sun) 45%, var(--sun-deep) 100%);
  }
  .brand {
    position: absolute;
    left: 518px;
    top: 0;
    width: 164px;
    height: 85px;
    background: var(--paper);
    display: flex;
    flex-direction: column;
    align-items: center;
    justify-content: center;
    gap: 5px;
    color: var(--brand-ink);
  }
  .brand__name {
    font-weight: 400;
    font-size: 15px;
    line-height: 1.1;
    text-align: center;
  }
  .brand__tagline {
    font-weight: 400;
    font-size: 8px;
  }
  .hero-photo {
    position: absolute;
    left: 270px;
    top: 95px;
    width: 663px;
    height: 418px;
    border-radius: 180px 180px 0 0;
    background: linear-gradient(180deg, #b98e74 0%, var(--skin-a) 45%, var(--skin-b) 100%);
  }
  .offer-card {
    position: absolute;
    left: 215px;
    top: 512px;
    width: 770px;
    height: 385px;
    border-radius: 27px;
    background: var(--paper);
    overflow: hidden;
    box-shadow: 0 28px 30px -12px rgba(120,60,0,0.35);
    text-align: center;
  }
  .offer-card__headline {
    margin-top: 52px;
    font-weight: 700;
    font-size: 39px;
    line-height: 1;
    color: var(--sun);
  }
  .offer-card__terms {
    margin-top: 20px;
    font-weight: 700;
    font-size: 40px;
    line-height: 48px;
    color: var(--ink);
    letter-spacing: -0.4px;
  }
  .offer-card__cta {
    position: absolute;
    left: 0;
    bottom: 0;
    width: 100%;
    height: 128px;
    background: var(--sun);
    color: var(--paper);
    font-weight: 700;
    font-size: 40px;
    display: flex;
    align-items: center;
    justify-content: center;
    padding-bottom: 6px;
  }
  .pointer {
    position: absolute;
    left: 590px;
    top: 858px;
    width: 108px;
    height: 108px;
  }
</style>
</head>
<body>
  <main class="ad">
    <div class="ad__backdrop" role="img" aria-label="Warm yellow halftone view of a bright treatment room"></div>

    <header class="brand">
      <p class="brand__name">Dewline<br>Aesthetics</p>
      <p class="brand__tagline">Glow Starts With Care</p>
    </header>

    <div class="hero-photo" role="img" aria-label="Three smiling women of diverse backgrounds with glowing skin, leaning together"></div>

    <section class="offer-card">
      <h1 class="offer-card__headline">$50 off the Velmira Treatment</h1>
      <p class="offer-card__terms">For first-time customers who<br>book a Velmira appointment</p>
      <a class="offer-card__cta">Make an appointment</a>
    </section>

    <svg class="pointer" viewBox="0 0 24 24" aria-hidden="true">
      <path d="M2 1 L2 19 L7 14.5 L10.5 22 L14 20.5 L10.5 13 L17 13 Z" fill="#ffffff" stroke="#000000" stroke-width="1.6" stroke-linejoin="miter"/>
    </svg>
  </main>
</body>
</html>
```